PowerPoint Design Project for Retirement Planning Company

Please design a powerpoint presentation template for our retirement planning company called Pine Harbor Advisors. We need a cover page and slide pages in both portrait and landscape orientation. We make many presentations to clients.

Our tagline is "Retirement Planning. Simplified." We are educators in the retirement planning space. Our company educates small and mid-sized businesses in the board room and break room on how to select a retirement plan for the company and their employees that will help them retire ready. Our slide deck needs to have appeal to a CEO in the board room and a blue collar worker in the breakroom.

We are looking for a template that incorporates our logo, tagline images, colors - green, gray and brown (see uploaded files for examples). The design needs to be clean with plenty of space for text. It needs to be crisp, modern, and eye catching.

We look forward to seeing how you use the images in our business card and logo to achieve a pleasing design. You are the experts so we hope you will develop some innovative designs that wow us and give our clients the confidence that we are experts and put together.
Updates

Designers - Thanks for your great work so far.  

Please do not include the website address on the powerpoint template.

Please provide one template per submission.  When they are grouped together, it is too hard to see the details on your slides.  

Thanks!

Target Market(s)

CEOs and Executive teams at small to medium sized businesses that care about their employees future retirement

Industry/Entity Type

Landscape

Requirements
Must have
• 1) Cover Page (should double as a report cover as well)

2) Second Page for text

3) Third Page for illustrations/graphs/charts

Landscape orientation and Portrait orientation

Colors:

Brown light : C=35, M=60, Y=80, K=25
Brown dark : C=40, M=70, Y=100, K=50

Gray Icon Border: C=0, M=0, Y=0, K=80
Gray Icon Background: C=0, M=0, Y=0, K=5
Gray Letters: C=0, M=0, Y=0, K=80
Gray Light Person: C=0, M=0, Y=0, K=40
Gray Dark Person: C=0, M=0, Y=0, K=60
Gray Dark Wheel Checked: C=0, M=0, Y=0, K=90

Green Light 1: C=40, M=8, Y=85, K=0
Green Light 2: C=53, M=17, Y=100, K=0
Green Dark: C=67, M=39, Y=100, K=27

White: C=0, M=0, Y=0, K=0

Black: C=0, M=0, Y=0, K=100

Fonts:
Logo and graphics files
Footlight MT Light
BrowalliaUPC

Business card/Letterhead files
Calisto MT
Segoe UI

Nice to have
• Please look at the back of our business card design. It has a version of our logo in an abstract form. Consider this concept in full color or a grayed out version as a backdrop.

Use of the "hill" with our tagline is another concept that could be incorporated into the design. See front of our business card and letterhead.

I have uploaded a diagram (wheel diagram full color) that we use to describe our services, plus all the images we use to describe our services (pdf). These images needs to look good as content on a slide.

```html
<!DOCTYPE html>
<html lang="en">
<head>
<meta charset="utf-8">
<title>Pine Harbor Advisors – Cover Slide</title>
<link rel="stylesheet" href="https://fonts.googleapis.com/css2?family=Cormorant+Garamond:wght@500;600&family=Open+Sans:wght@400&display=swap">
<style>
  :root {
    --green-dark: #3f5a25;
    --green-mid: #5a7a35;
    --green-deep: #2a3418;
    --green-text: #6f8f3a;
    --gray-text: #8a8a8a;
    --gray-deco: #c6c6c6;
    --gray-deco-soft: #d6d6d6;
    --white: #ffffff;
  }
  html, body {
    margin: 0;
    padding: 0;
    width: 1200px;
    height: 901px;
    overflow: hidden;
    background: var(--white);
  }
  .slide {
    position: relative;
    width: 1200px;
    height: 901px;
    overflow: hidden;
    background: var(--white);
  }
  .slide__backdrop {
    position: absolute;
    left: -230px;
    top: 150px;
    width: 800px;
    height: 800px;
    border-radius: 50%;
    background: radial-gradient(circle at 50% 50%,
      var(--gray-deco) 0%,
      var(--gray-deco) 38%,
      var(--gray-deco-soft) 62%,
      rgba(214,214,214,0.55) 74%,
      rgba(255,255,255,0) 82%);
  }
  .slide__header {
    position: absolute;
    top: 0;
    left: 0;
    width: 1200px;
    height: 170px;
  }
  .slide__tagline {
    position: absolute;
    left: 36px;
    top: 42px;
    margin: 0;
    font-family: "Cormorant Garamond", serif;
    font-weight: 600;
    font-size: 46px;
    font-variant: small-caps;
    letter-spacing: 0.3px;
    color: var(--white);
    line-height: 1;
  }
  .slide__title {
    position: absolute;
    right: 20px;
    top: 322px;
    margin: 0;
    text-align: right;
    font-family: "Cormorant Garamond", serif;
    font-weight: 500;
    font-size: 52px;
    line-height: 58px;
    color: var(--green-text);
  }
  .slide__subtitle {
    position: absolute;
    right: 20px;
    top: 480px;
    margin: 0;
    text-align: right;
    font-family: "Open Sans", sans-serif;
    font-weight: 400;
    font-size: 33px;
    line-height: 38px;
    color: var(--gray-text);
  }
  .brand {
    position: absolute;
    left: 738px;
    top: 752px;
    display: flex;
    align-items: center;
    gap: 14px;
  }
  .brand__dot {
    width: 124px;
    height: 124px;
    border-radius: 50%;
    background: var(--green-dark);
  }
  .brand__name {
    font-family: "Cormorant Garamond", serif;
    font-weight: 600;
    font-size: 46px;
    line-height: 46px;
    color: var(--green-deep);
  }
  .slide__footer-bar {
    position: absolute;
    left: 0;
    bottom: 0;
    width: 1200px;
    height: 10px;
    background: var(--green-dark);
  }
</style>
</head>
<body>
<main class="slide">
  <div class="slide__backdrop" role="img" aria-label="Large faint gray circular brand backdrop"></div>

  <svg class="slide__header" viewBox="0 0 1200 170" aria-hidden="true">
    <defs>
      <radialGradient id="headerGlow" cx="42%" cy="10%" r="70%">
        <stop offset="0%" stop-color="#5f7f36"/>
        <stop offset="100%" stop-color="#34491c"/>
      </radialGradient>
    </defs>
    <path d="M0 0 H1200 V55 Q 700 150 260 140 Q 120 130 0 100 Z" fill="url(#headerGlow)"/>
    <path d="M260 143 Q 800 158 1200 70 V110 Q 800 162 260 143 Z" fill="var(--green-deep)"/>
    <path d="M260 140 Q 800 150 1200 58 V66 Q 800 156 260 141 Z" fill="#ffffff" opacity="0.9"/>
  </svg>

  <p class="slide__tagline">Retirement plans. Simplified.</p>

  <h1 class="slide__title">Lorem ipsum dolor sit<br>amet, consectetur</h1>
  <p class="slide__subtitle">Pellentesque ac risus nulla,<br>nec porta velit</p>

  <div class="brand">
    <div class="brand__dot"></div>
    <div class="brand__name">Pine Harbor<br>Advisors</div>
  </div>

  <div class="slide__footer-bar"></div>
</main>
</body>
</html>
```